Corporate Business Card Design Project

..Hi designers!
I have established a consultancy within strategic communnications, for which I need a business card design - I've seen some of the things you do in here, and they're great! I'll provide some information in the following:
Name: BriarLedger
Tagline: Guiding Dialogue
Service: Strategic communications consulting (primariy internal communication and optimizing): various organisations - e.g. SMEs, NGOs and NPOs - are offered an analysis of their current efforts and, on the basis of that, management consulting tailored their unique challenges and needs.
It's a sole proprietorship - for now! - but it's my plan to employ 5-20 persons over the years. Therefore the card should NOT symbolize a start-up, but communicate a well-established, serious consultancy. Hence, it should also apply to serious companies and organizations - think Veltra or Hollis Brant Group (both as sender and receiver) ;)
The design should accordingly have a formal, conservative, stylish, corporate, clean look! and ditto colors, eg. black, grey, white etc - corresponding to the logo. The only colour that can appear is the same orange contrast as in my logo (see attachement). Not too bold or dramatic fonds or letters.
I choose the double sided as I think it gives the most professional look: One side with name, titel, phone, e-mail - then a little space - and four additional lines for address.
This composition is if all information should be in the same "column" - feel free to provide suggestions with the address places elsewhere on the one side.
On the other side, I'm only thinkin' something with the logo.
I'd be happy to see different ideas re. the use of the orange contrast, placement of logo, etc.
I do not plan on changing the design of businees cards ever - as I think it is more serious keeping a concept and avoid rebranding - and I'm sure that you can deliver an ever-lasting logo for my company! Thanks :).
Let's play the rest by ear in the correspondance.
Target Market(s)
Executive level: CEOs, HR directors, communication managers/directors, business owners.
Industry/Entity Type
Management Consulting

```html
<!DOCTYPE html>
<html lang="en">
<head>
<meta charset="utf-8">
<title>BriarLedger — Business Card</title>
<link rel="stylesheet" href="https://fonts.googleapis.com/css2?family=Gelasio:wght@400&family=Marcellus+SC&display=swap">
<style>
  :root {
    --page: #ffffff;
    --ink-navy: #05040f;
    --accent-orange: #f26a12;
    --text-light: #ffffff;
    --text-dark: #111111;
  }
  html, body {
    margin: 0;
    padding: 0;
    width: 1200px;
    height: 848px;
    overflow: hidden;
    background: var(--page);
  }
  .canvas {
    position: relative;
    width: 1200px;
    height: 848px;
    background: var(--page);
  }
  .card {
    position: absolute;
    top: 283px;
    width: 493px;
    height: 281px;
    overflow: hidden;
  }
  .card--front { left: 103px; background: var(--ink-navy); }
  .card--back  { left: 604px; background: var(--accent-orange); }

  .brand {
    position: absolute;
    left: 56px;
    top: 40px;
  }
  .brand__name {
    display: block;
    font-family: "Gelasio", Georgia, serif;
    font-size: 31px;
    line-height: 1;
    letter-spacing: -0.3px;
  }
  .brand__tagline {
    display: block;
    margin: 3px 0 0 92px;
    font-family: "Gelasio", Georgia, serif;
    font-size: 9px;
    letter-spacing: 1.1px;
    line-height: 1;
  }
  .card--front .brand__name,
  .card--front .brand__tagline { color: var(--text-light); }
  .card--back .brand { left: 40px; }
  .card--back .brand__name { color: var(--text-dark); }
  .card--back .brand__tagline { color: var(--text-light); }

  .contact {
    position: absolute;
    left: 57px;
    top: 175px;
    font-family: "Marcellus SC", "Times New Roman", serif;
    color: var(--text-light);
    font-size: 11.5px;
    line-height: 15px;
    letter-spacing: 0.4px;
  }
  .contact p { margin: 0; }
  .contact__name { font-weight: bold; }
  .contact__details { margin-top: 23px !important; }

  .service-band {
    position: absolute;
    left: 0;
    top: 176px;
    width: 100%;
    height: 46px;
    background: var(--ink-navy);
    display: flex;
    align-items: center;
    justify-content: center;
  }
  .service-band__text {
    margin: 0;
    font-family: "Marcellus SC", "Times New Roman", serif;
    color: var(--accent-orange);
    font-size: 17px;
    letter-spacing: 1px;
  }
</style>
</head>
<body>
<main class="canvas">
  <section class="card card--front" aria-label="Business card front">
    <div class="brand">
      <span class="brand__name">BriarLedger</span>
      <span class="brand__tagline">Guiding Dialogue</span>
    </div>
    <div class="contact">
      <p class="contact__name">Dr. Name Surname</p>
      <p class="contact__role">Position</p>
      <div class="contact__details">
        <p>Phone: 555-201-4837 -&nbsp; 555-201-4862</p>
        <p>Office address 2781&nbsp; Alder Rd. Fairmont Ks 60418</p>
      </div>
    </div>
  </section>

  <section class="card card--back" aria-label="Business card back">
    <div class="brand">
      <span class="brand__name">BriarLedger</span>
      <span class="brand__tagline">Guiding Dialogue</span>
    </div>
    <div class="service-band">
      <p class="service-band__text">Strategic communications consulting</p>
    </div>
  </section>
</main>
</body>
</html>
```